New Graphic Design Project / Email signiture and Letterhead

I would like a new SIMPLE but high end quality modern/heavy industrial design for an email Signiture and letter head that incorporates product photos or illustrations of our products to show our customers our range of products and also show our head office in Perth Western Australia and also our Australian and international reseller locations.
in my present email signature you would see that I have other company logos these companies are old partners of ours but some are no longer so I would like to have the option to add and change them if things change in the future.
for ideas Our main products are as follows
Composite Hose
Convoluted hose
Metal expansion joints
Fabric expansion joints
Rubber Expansion joints
Please see our website for ideas and our product photos.
www.dravoline.com.au
if you need any further information please let me know
i have attached our old email signiture for reference.
Mark

Target Market(s)

Oil and Gas / Mining / Petroleum and Chemical Refineries, high end engineering

Requirements
Must have
• pictures / photos of our core products and our company capabilities to show our existing and new customers what we can do.
in the email signature - links to company face book and LinkedIn, our website
I would like to have spaces for my company partners logos and need the final file to be in a format for me to change and update all details
All so our Font is Conthrax SB
Nice to have
• the email signature, I would like this to have all the required information ( as per attached present email signature ) but also be informative / marketing to show customers what we do if possible.
the letter head can be based from the same but simple with or without product photos

```html
<!DOCTYPE html>
<html lang="en">
<head>
<meta charset="utf-8">
<title>Dravoline Letterhead</title>
<link rel="stylesheet" href="https://fonts.googleapis.com/css2?family=Lato:wght@400;700&family=Encode+Sans+Semi+Condensed:wght@300;400&display=swap">
<style>
  :root {
    --backdrop: #d9d9d9;
    --paper: #ffffff;
    --ink: #4a4a4a;
    --ink-strong: #111111;
    --ink-soft: #6b6b6b;
    --band-dark: #141414;
    --badge-red: #d9272e;
    --badge-navy: #1f3a6e;
    --badge-grey: #9a9a9a;
    --badge-gold: #c9a64a;
  }
  * { box-sizing: border-box; margin: 0; padding: 0; }
  html, body {
    width: 1056px; height: 1200px; overflow: hidden;
    background: var(--backdrop);
  }
  .letterhead {
    position: absolute; left: 118px; top: 20px;
    width: 820px; height: 1160px;
    background: var(--paper);
    color: var(--ink);
    overflow: hidden;
  }
  .brand {
    position: absolute; left: 75px; top: 86px;
    display: flex; align-items: center; gap: 12px;
  }
  .brand-dot {
    width: 58px; height: 58px; border-radius: 50%;
    background: var(--ink);
  }
  .brand-name {
    font-family: "Lato", sans-serif; font-weight: 700;
    font-size: 36px; letter-spacing: 1px; color: var(--ink);
  }
  .contact {
    position: absolute; left: 602px; top: 56px; width: 205px;
    font-family: "Lato", sans-serif; font-style: normal;
    font-size: 12.5px; line-height: 16.5px;
    color: var(--ink-soft);
  }
  .contact b { color: var(--ink-strong); font-weight: 700; }
  .contact p { margin-bottom: 2px; }
  .contact-line { display: flex; align-items: center; gap: 14px; height: 19px; }
  .contact-line svg { width: 13px; height: 13px; fill: var(--ink-strong); flex: none; }
  .letter {
    position: absolute; left: 75px; top: 351px; width: 666px;
    font-family: "Encode Sans Semi Condensed", sans-serif; font-weight: 300;
    font-size: 17.5px; line-height: 28.5px; color: var(--ink);
  }
  .letter p { text-align: justify; margin-bottom: 28.5px; }
  .sign-off {
    position: absolute; left: 75px; top: 934px;
    font-family: "Encode Sans Semi Condensed", sans-serif; font-weight: 300;
    font-size: 17.5px; color: var(--ink);
  }
  .signature {
    position: absolute; left: 77px; top: 970px; width: 132px; height: 40px;
    background: linear-gradient(90deg, rgba(34,34,34,0.10), rgba(34,34,34,0.04));
    border-radius: 4px;
  }
  .partners {
    position: absolute; left: 26px; top: 1082px; width: 770px; height: 38px;
    display: flex; justify-content: space-between; align-items: center;
  }
  .badge { height: 28px; border-radius: 3px; }
  .badge.wide { width: 140px; }
  .badge.mid { width: 82px; }
  .badge.small { width: 46px; }
  .badge.round { width: 36px; height: 36px; border-radius: 50%; }
  .bg-red { background: var(--badge-red); }
  .bg-navy { background: var(--badge-navy); }
  .bg-grey { background: var(--badge-grey); }
  .bg-gold { background: var(--badge-gold); }
  .footer-band {
    position: absolute; left: 0; bottom: 0; width: 820px; height: 24px;
    background: var(--band-dark);
    display: flex; align-items: center; justify-content: flex-end;
    padding-right: 27px;
  }
  .footer-web {
    font-family: "Lato", sans-serif; font-size: 13px; color: #ffffff;
  }
</style>
</head>
<body>
<main class="letterhead">
  <header>
    <div class="brand">
      <span class="brand-dot"></span>
      <span class="brand-name">DRAVOLINE</span>
    </div>
    <address class="contact">
      <p><b>Head Office:</b> 42 Ferrous Way Kewdale, WA 6105</p>
      <p><b>Locations:</b> Australia, Singapore, Indonesia, Vietnam</p>
      <div class="contact-line">
        <svg viewBox="0 0 16 16" aria-hidden="true"><path d="M3 1l3 3-2 2c1 2 3 4 5 5l2-2 3 3-2 2C7 15 1 9 1 3z"/></svg>
        <span>+614 55 210 384</span>
      </div>
      <div class="contact-line">
        <svg viewBox="0 0 16 16" aria-hidden="true"><path d="M4 1h8v4H4zM1 6h14v6h-3v3H4v-3H1zM5 10v4h6v-4z"/></svg>
        <span>+614 55 210 399</span>
      </div>
      <div class="contact-line">
        <svg viewBox="0 0 16 16" aria-hidden="true"><path d="M1 3h14v10H1zM2 4l6 5 6-5v-0.5H2z" fill-rule="evenodd"/></svg>
        <span>mark@dravoline.com.au</span>
      </div>
    </address>
  </header>

  <section class="letter">
    <p>Dear Sir/Mam,</p>
    <p>Contrary to popular belief, Lorem Ipsum is not simply random text. It has roots in a piece of classical Latin literature from 45 BC, making it over 2000 years old. Richard Ellsworth, a Latin professor at Ashcombe College in Virginia, looked up one of the more obscure Latin words, consectetur.</p>
    <p>Lorem Ipsum comes from sections 1.10.32 and 1.10.33 of "de Finibus Bonorum et Malorum" (The Extremes of Good and Evil) by Tenax, written in 45 BC. This book is a treatise on the theory of ethics, very popular during the Renaissance. The first line of Lorem Ipsum.</p>
    <p>The standard chunk of Lorem Ipsum used since the 1500s is reproduced below for those interested. Sections 1.10.32 and 1.10.33 from "de Finibus Bonorum et Malorum" by Tenax are also reproduced in their exact original.</p>
    <p>The standard chunk of Lorem Ipsum used since the 1500s is reproduced below for those interested.</p>
  </section>

  <p class="sign-off">Best Regards</p>
  <div class="signature" role="img" aria-label="Handwritten signature of Mark Holloway"></div>

  <footer>
    <div class="partners" aria-label="Partner badges">
      <span class="badge wide bg-red"></span>
      <span class="badge mid bg-navy"></span>
      <span class="badge small bg-grey"></span>
      <span class="badge small bg-navy"></span>
      <span class="badge small bg-grey"></span>
      <span class="badge mid bg-navy"></span>
      <span class="badge round bg-grey"></span>
      <span class="badge wide bg-gold"></span>
    </div>
    <div class="footer-band">
      <span class="footer-web">www.dravoline.com.au</span>
    </div>
  </footer>
</main>
</body>
</html>
```